Criação de Kit Layout de Posts para Redes Sociais (Facebook, Instagram e etc) para Esportes
" Ofereço serviços de personal trainer para alunos em academias, condomínios, parques, etc.; serviços de personal trainer on-line ao vivo; e serviços de consultoria para prescrição de treinos (sem o acompanhamento durante a execução em si dos treinos) "

```html
<!DOCTYPE html>
<html lang="pt-BR">
<head>
<meta charset="utf-8">
<title>Kit de posts – Rafael Moreno Personal Trainer</title>
<link rel="stylesheet" href="https://fonts.googleapis.com/css2?family=Montserrat:ital,wght@0,600;0,700;0,800;0,900;1,800&display=swap">
<style>
  :root{
    --page:#ffffff;
    --ink-dark:#0d1a10;
    --forest:#10301a;
    --forest-deep:#0a2012;
    --green:#5cbf2a;
    --green-soft:#7fd63f;
    --frame:#4e9e2a;
    --white:#ffffff;
    --body-font:'Montserrat', Arial, sans-serif;
  }
  *{box-sizing:border-box;margin:0;padding:0}
  html,body{width:1200px;height:1200px;overflow:hidden;background:var(--page)}
  body{font-family:var(--body-font)}
  .kit{
    width:1200px;height:1200px;padding:14px;
    display:grid;grid-template-columns:1fr 1fr;grid-template-rows:1fr 1fr;gap:18px;
  }
  .post{
    position:relative;overflow:hidden;
    border:4px solid var(--frame);
    background:var(--forest-deep);
  }
  .post__photo{position:absolute;inset:0}
  .post--shape .post__photo{background:
    radial-gradient(ellipse 30% 48% at 48% 35%, #c98f6c 0%, #8e5a3e 45%, transparent 75%),
    radial-gradient(ellipse 28% 52% at 80% 40%, #b8805c 0%, #6a3d28 50%, transparent 78%),
    linear-gradient(160deg,#1c2a20 0%,#0d1810 100%)}
  .post--search .post__photo{background:
    radial-gradient(ellipse 40% 55% at 68% 42%, #b58a6a 0%, #4c3a2e 50%, transparent 78%),
    linear-gradient(170deg,#2a322c 0%,#101612 100%)}
  .post--focus .post__photo{background:
    radial-gradient(ellipse 36% 58% at 55% 35%, #d9a07a 0%, #9b6444 45%, transparent 78%),
    linear-gradient(160deg,#3a4a3c 0%,#141d16 100%)}
  .post--barriers .post__photo{background:
    radial-gradient(ellipse 30% 45% at 70% 55%, #b08866 0%, #54402f 50%, transparent 78%),
    radial-gradient(ellipse 60% 40% at 60% 20%, #6c6a5e 0%, transparent 70%),
    linear-gradient(170deg,#3c3f38 0%,#151814 100%)}
  .post__shapes{position:absolute;inset:0;width:100%;height:100%}
  .post__shade{position:absolute;inset:0;
    background:linear-gradient(90deg,rgba(8,20,12,.78) 0%,rgba(8,20,12,.35) 55%,rgba(8,20,12,0) 80%)}

  .brand{
    position:absolute;left:14px;top:12px;
    width:188px;height:62px;padding:8px 12px;
    background:var(--forest);border-bottom:3px solid var(--green);
    display:flex;flex-direction:column;align-items:center;justify-content:center;gap:2px;
  }
  .brand__mark{width:14px;height:14px;background:var(--green)}
  .brand__name{color:var(--white);font-weight:700;font-size:13px;letter-spacing:.5px;text-transform:uppercase;line-height:1}
  .brand__role{color:var(--white);font-weight:700;font-size:7px;letter-spacing:1.6px;text-transform:uppercase;line-height:1}

  .headline{
    position:absolute;left:24px;
    color:var(--white);font-weight:900;font-size:52px;line-height:1;letter-spacing:.5px;
    text-transform:uppercase;text-shadow:0 3px 6px rgba(0,0,0,.55);
  }
  .tagline{
    position:absolute;left:26px;
    color:var(--green-soft);font-weight:800;font-size:19px;line-height:1.22;
    text-shadow:0 2px 4px rgba(0,0,0,.6);
  }
  .goals{list-style:none;display:grid;grid-template-columns:auto auto;column-gap:14px;width:270px;font-size:21px}
  .goals li:nth-child(n+3){grid-column:1 / span 2}

  .cta{
    position:absolute;left:0;width:272px;height:38px;
    background:var(--green);color:var(--forest-deep);
    clip-path:polygon(0 0,100% 0,calc(100% - 20px) 100%,0 100%);
    display:flex;align-items:center;padding-left:40px;
    font-weight:900;font-size:15px;letter-spacing:.6px;text-transform:uppercase;
  }
  .contacts{position:absolute;left:26px;list-style:none;color:var(--white);font-weight:700;font-size:12.5px;line-height:1.5}
  .contacts li{display:flex;align-items:center;gap:6px}
  .contacts svg{width:11px;height:11px;fill:var(--green)}
</style>
</head>
<body>
<main class="kit">

  <!-- Post 1 -->
  <article class="post post--shape">
    <div class="post__photo" role="img" aria-label="Foto de um casal de atletas musculosos, homem e mulher em roupa de treino"></div>
    <div class="post__shade"></div>
    <svg class="post__shapes" viewBox="0 0 569 569" preserveAspectRatio="none" aria-hidden="true">
      <polygon points="0,330 230,569 0,569" fill="#16401f" opacity=".85"/>
      <polygon points="300,569 569,300 569,569" fill="#1d5a27" opacity=".55"/>
      <polygon points="440,0 569,0 569,130" fill="#1d5a27" opacity=".5"/>
    </svg>
    <div class="brand"><span class="brand__mark"></span><span class="brand__name">Rafael Moreno</span><span class="brand__role">Personal Trainer</span></div>
    <h2 class="headline" style="top:208px">De forma a<br>seu corpo</h2>
    <p class="tagline" style="top:330px">Evolução mais rápida com<br>instruções correta</p>
    <div class="cta" style="top:414px">Entre em contato</div>
    <ul class="contacts" style="top:462px">
      <li><svg viewBox="0 0 24 24"><path d="M6.6 10.8a15 15 0 0 0 6.6 6.6l2.2-2.2c.3-.3.7-.4 1-.2 1.1.4 2.3.6 3.6.6.6 0 1 .4 1 1V20c0 .6-.4 1-1 1A17 17 0 0 1 3 4c0-.6.4-1 1-1h3.5c.6 0 1 .4 1 1 0 1.3.2 2.5.6 3.6.1.3 0 .7-.2 1z"/></svg>11 95550-4183</li>
      <li><svg viewBox="0 0 24 24"><circle cx="12" cy="12" r="10"/></svg>@personal_rafaelmoreno</li>
      <li><svg viewBox="0 0 24 24"><path d="M2 5h20v14H2zM3.5 6.5 12 13l8.5-6.5z"/></svg>personal.rafael@mailbox.com</li>
    </ul>
  </article>

  <!-- Post 2 -->
  <article class="post post--search">
    <div class="post__photo" role="img" aria-label="Foto de uma mulher fazendo alongamento em pé, segurando a perna estendida para cima, em academia escura"></div>
    <div class="post__shade"></div>
    <svg class="post__shapes" viewBox="0 0 569 569" preserveAspectRatio="none" aria-hidden="true">
      <polygon points="0,330 230,569 0,569" fill="#16401f" opacity=".85"/>
      <polygon points="380,0 569,0 569,190" fill="#1d5a27" opacity=".45"/>
      <polygon points="330,569 569,330 569,569" fill="#1d5a27" opacity=".45"/>
    </svg>
    <div class="brand"><span class="brand__mark"></span><span class="brand__name">Rafael Moreno</span><span class="brand__role">Personal Trainer</span></div>
    <h2 class="headline" style="top:208px">Qual a<br>sua busca?</h2>
    <ul class="tagline goals" style="top:330px">
      <li>*Saúde</li><li>*Bem-estar</li><li>*longevidade</li><li>*Qualidade de vida</li>
    </ul>
    <div class="cta" style="top:436px">Entre em contato</div>
    <ul class="contacts" style="top:482px">
      <li><svg viewBox="0 0 24 24"><path d="M6.6 10.8a15 15 0 0 0 6.6 6.6l2.2-2.2c.3-.3.7-.4 1-.2 1.1.4 2.3.6 3.6.6.6 0 1 .4 1 1V20c0 .6-.4 1-1 1A17 17 0 0 1 3 4c0-.6.4-1 1-1h3.5c.6 0 1 .4 1 1 0 1.3.2 2.5.6 3.6.1.3 0 .7-.2 1z"/></svg>11 95550-4183</li>
      <li><svg viewBox="0 0 24 24"><circle cx="12" cy="12" r="10"/></svg>@personal_rafaelmoreno</li>
      <li><svg viewBox="0 0 24 24"><path d="M2 5h20v14H2zM3.5 6.5 12 13l8.5-6.5z"/></svg>personal.rafael@mailbox.com</li>
    </ul>
  </article>

  <!-- Post 3 -->
  <article class="post post--focus">
    <div class="post__photo" role="img" aria-label="Foto do tronco de uma mulher em top esportivo, mãos na cintura, mostrando o abdômen"></div>
    <div class="post__shade"></div>
    <svg class="post__shapes" viewBox="0 0 569 569" preserveAspectRatio="none" aria-hidden="true">
      <polygon points="0,380 190,569 0,569" fill="#16401f" opacity=".85"/>
      <polygon points="420,0 569,0 569,150" fill="#1d5a27" opacity=".5"/>
      <polygon points="360,569 569,360 569,569" fill="#1d5a27" opacity=".45"/>
    </svg>
    <div class="brand"><span class="brand__mark"></span><span class="brand__name">Rafael Moreno</span><span class="brand__role">Personal Trainer</span></div>
    <h2 class="headline" style="top:292px">Foco e<br>determinação</h2>
    <p class="tagline" style="top:410px">Controle total do CORPO<br>e da MENTE</p>
    <div class="cta" style="top:462px">Entre em contato</div>
    <ul class="contacts" style="top:504px">
      <li><svg viewBox="0 0 24 24"><path d="M6.6 10.8a15 15 0 0 0 6.6 6.6l2.2-2.2c.3-.3.7-.4 1-.2 1.1.4 2.3.6 3.6.6.6 0 1 .4 1 1V20c0 .6-.4 1-1 1A17 17 0 0 1 3 4c0-.6.4-1 1-1h3.5c.6 0 1 .4 1 1 0 1.3.2 2.5.6 3.6.1.3 0 .7-.2 1z"/></svg>11 95550-4183</li>
      <li><svg viewBox="0 0 24 24"><circle cx="12" cy="12" r="10"/></svg>@personal_rafaelmoreno</li>
      <li><svg viewBox="0 0 24 24"><path d="M2 5h20v14H2zM3.5 6.5 12 13l8.5-6.5z"/></svg>personal.rafael@mailbox.com</li>
    </ul>
  </article>

  <!-- Post 4 -->
  <article class="post post--barriers">
    <div class="post__photo" role="img" aria-label="Foto de uma mulher fazendo agachamento com peso em academia iluminada"></div>
    <div class="post__shade"></div>
    <svg class="post__shapes" viewBox="0 0 569 569" preserveAspectRatio="none" aria-hidden="true">
      <polygon points="0,300 250,569 0,569" fill="#16401f" opacity=".85"/>
      <polygon points="400,0 569,0 569,170" fill="#1d5a27" opacity=".45"/>
      <polygon points="340,569 569,340 569,569" fill="#1d5a27" opacity=".45"/>
    </svg>
    <div class="brand"><span class="brand__mark"></span><span class="brand__name">Rafael Moreno</span><span class="brand__role">Personal Trainer</span></div>
    <h2 class="headline" style="top:196px">Atravesse<br>barreiras</h2>
    <p class="tagline" style="top:312px;font-size:17px">Todo apoio correto para manter<br>seus treinos saudáveis</p>
    <div class="cta" style="top:400px">Entre em contato</div>
    <ul class="contacts" style="top:448px">
      <li><svg viewBox="0 0 24 24"><path d="M6.6 10.8a15 15 0 0 0 6.6 6.6l2.2-2.2c.3-.3.7-.4 1-.2 1.1.4 2.3.6 3.6.6.6 0 1 .4 1 1V20c0 .6-.4 1-1 1A17 17 0 0 1 3 4c0-.6.4-1 1-1h3.5c.6 0 1 .4 1 1 0 1.3.2 2.5.6 3.6.1.3 0 .7-.2 1z"/></svg>11 95550-4183</li>
      <li><svg viewBox="0 0 24 24"><circle cx="12" cy="12" r="10"/></svg>@personal_rafaelmoreno</li>
      <li><svg viewBox="0 0 24 24"><path d="M2 5h20v14H2zM3.5 6.5 12 13l8.5-6.5z"/></svg>personal.rafael@mailbox.com</li>
    </ul>
  </article>

</main>
</body>
</html>
```